Vergleichsportal für Reparaturen benötigt Flyer-Design
Zielgruppe
Wir sind ein Vergleichsportal für Reparaturen. Auf unserem Portal können sich Reparaturwerkstätten anmelden und deren Dienstleistungen mit Preisen hinterlegen. Der Kunde wählt das zu reparierende Gerät aus und gibt seine Adresse ein. Anschließend bekommt der Kunde alle Werkstätten nach Entfernung zum Kunden angezeigt mit den Reparaturpreisen. Der Kunde wählt seine Werkstatt aus und bezahlt den Reparaturpreis direkt auf unseren Portal. Die Zahlung geht auf ein Treuhandkonto. Der Kunde gibt das Gerät an die ausgewählt Werkstatt ab und erst wenn der Kunde mit der Reparatur zufrieden war, wird der Reparaturbetrag an die Werkstatt vom Kunden freigegeben.
Unsere Zielgruppe sind Kunden im Alter von 18 bis 40 Jahren und Technikaffine. Darunter Qualitätsbewusste Kunde sowie Schnäppchenjäger. Unsere Webseite lautet: flickwerkstube.de
Aufgabenstellung
Das Design sollte ansprechend sein und Interesse beim Kunden wecken. Die Farbe sollte unserer Webseite entsprechen. Es können auch Elemente von der Webseite übernommen werden wie z. B. die Vergleichseite etc.
Auf der Vorderseite sollte die Vorteile abgebildet werden.
- Finde deine Werkstatt in deiner Nähe
- Vergleiche die Qualität und Preise der Werkstätten
- Online Best Preis sichern und lokal reparieren lassen
- Abgesichert durch den Kaufhort Siegel Käuferschutz
- Sichere Zahlung über MUNDOR Treuhandschutz
Noch ein Call To Action/Störer einbauen. 'Jetzt Gutschein nutzen und sparen'
Auf der Rückseite sollte Gutscheine bzw. Coupons abgebildet sein.
ca. 6 Gutscheine mit unterschiedlichen Angeboten.
z. B. Displayreparatur
Velkor Modelle
10 Euro
Gutscheincode
Weiterhin sollte die Siegel drauf sein. Gerne auf beiden Seiten. Und ganz unten auf der Rückseite sollte Platz für den Rechtstext sein.
Gerne können eigene Idee mit einfließen.
Ich freue mich auf deinen Flyer.
Vielen DANK im Voraus

```html
<!DOCTYPE html>
<html lang="de">
<head>
<meta charset="utf-8">
<title>flickwerkstube – Flyer Vorder- und Rückseite</title>
<link href="https://fonts.googleapis.com/css2?family=Raleway:wght@300;400;500;600;700;800&display=swap" rel="stylesheet">
<style>
:root{
  --green:#7dbb3a;
  --green-light:#a6d46f;
  --teal:#1f4a5a;
  --teal-dark:#173b48;
  --ink:#2a3b44;
  --grey-band:#e9e9e9;
  --line:#c9cfd2;
  --bg:#dcdcdc;
  --white:#ffffff;
}
*{box-sizing:border-box;margin:0;padding:0}
html,body{width:750px;height:1200px;overflow:hidden}
body{background:var(--bg);font-family:"Raleway",sans-serif;color:var(--ink);position:relative}
.flyer{position:absolute;top:231px;width:345px;height:738px;background:var(--white);overflow:hidden;box-shadow:0 1px 3px rgba(0,0,0,.12)}
.flyer--front{left:20px}
.flyer--back{left:385px}
.band-top{position:absolute;left:0;top:0;width:100%;height:7px;background:var(--green)}
.flyer--back .band-top{background:var(--teal)}
.band-bottom{position:absolute;left:0;bottom:0;width:100%;height:13px;background:var(--green)}
.side-bar{position:absolute;left:0;top:7px;width:27px;height:718px;background:var(--teal)}
.hero-photo{position:absolute;left:27px;top:7px;width:318px;height:209px;
  background:linear-gradient(160deg,#5d666b 0%,#9aa2a6 35%,#d6dadc 60%,#aeb5b8 80%,#eef0f1 100%)}
.brand{position:absolute;font-family:"Raleway",sans-serif;font-weight:400;color:var(--teal);font-size:22px;letter-spacing:.3px;display:flex;align-items:center;gap:6px}
.brand__dot{width:14px;height:14px;border-radius:50%;background:var(--green)}
.flyer--front .brand{right:18px;top:46px}
.flyer--back .brand{left:0;right:0;justify-content:center;top:52px}
.claim{position:absolute;left:164px;top:109px;width:167px;height:39px;background:var(--teal);border-radius:3px;
  color:var(--white);text-align:center;font-weight:600;font-size:12.5px;line-height:15px;padding-top:4px}
.claim span{display:block;color:var(--green-light);font-weight:700}
.section-label{position:absolute;background:var(--white);border:2px solid var(--green);border-radius:2px;
  color:var(--teal);font-weight:700;text-align:center}
.flyer--front .section-label{left:65px;top:200px;width:133px;height:29px;font-size:19px;line-height:25px}
.flyer--back .section-label{left:79px;top:109px;width:186px;height:33px;font-size:20px;line-height:29px}
.stoerer{position:absolute;left:229px;top:171px;width:86px;height:86px;border-radius:50%;background:var(--green);
  border:3px solid var(--white);box-shadow:0 0 0 1.5px var(--green);color:var(--white);text-align:center;
  font-size:8.5px;font-weight:600;line-height:10px;padding-top:14px;text-transform:uppercase}
.stoerer b{display:block;font-size:15px;line-height:16px;font-weight:500;margin-bottom:3px}
.benefits{position:absolute;left:0;top:248px;width:345px;list-style:none}
.benefit{position:relative;height:67px}
.benefit__icon{position:absolute;left:11px;top:1px;width:43px;height:43px;border-radius:50%;background:var(--white);
  border:1.5px solid var(--line);display:flex;align-items:center;justify-content:center}
.benefit__title{position:absolute;left:66px;top:9px;color:var(--green);font-weight:600;font-size:13.5px;letter-spacing:.2px}
.benefit__text{position:absolute;left:66px;top:26px;font-size:10.3px;color:var(--ink);white-space:nowrap}
.benefit__rule{position:absolute;left:34px;top:57px;width:130px;height:1px;background:linear-gradient(90deg,transparent,#b9dd92,transparent)}
.seal-band{position:absolute;left:27px;top:601px;width:318px;height:44px;background:var(--grey-band)}
.flyer--back .seal-band{left:0;width:345px}
.seal{position:absolute;top:583px;width:64px;height:64px;border-radius:50%;background:var(--white);border:2px solid var(--teal)}
.flyer--front .seal--kaufhort{left:106px}
.flyer--front .seal--mundor{left:189px}
.flyer--back .seal--kaufhort{left:96px}
.flyer--back .seal--mundor{left:179px}
.url-box{position:absolute;top:661px;height:24px;background:var(--teal);color:var(--white);font-weight:600;font-size:11px;
  text-align:center;line-height:24px;letter-spacing:.2px}
.flyer--front .url-box{left:85px;width:195px}
.flyer--back .url-box{left:75px;width:195px}
.contacts{position:absolute;top:696px;display:flex;gap:12px;font-size:8px;line-height:9.5px;color:var(--ink)}
.flyer--front .contacts{left:37px}
.flyer--back .contacts{left:24px}
.contact{display:flex;align-items:center;gap:5px}
.contact__icon{width:16px;height:16px;border-radius:50%;border:1.3px solid var(--green);display:flex;align-items:center;justify-content:center;flex:none}
.cracks{position:absolute;left:0;top:7px;width:345px;height:200px;background:linear-gradient(180deg,#f6f7f7,#fff)}
.intro{position:absolute;left:20px;right:20px;top:162px;text-align:center;font-size:7.2px;line-height:9px;color:var(--ink)}
.coupon{position:absolute;width:146px;height:71px}
.coupon__box{position:absolute;left:0;top:0;width:146px;height:71px;border:1.3px solid var(--teal);border-radius:3px;background:var(--white)}
.coupon__value{position:absolute;left:-6px;top:-11px;width:67px;height:67px;border-radius:50%;background:var(--green);color:var(--white);
  text-align:center;font-weight:700;padding-top:13px;border:2px solid var(--white)}
.coupon__value b{display:block;font-size:22px;line-height:22px;letter-spacing:.5px}
.coupon__value span{display:block;font-size:12.5px;line-height:14px;font-weight:500}
.coupon__offer{position:absolute;left:64px;top:9px;width:80px;text-align:center;font-weight:700;color:var(--teal);font-size:10px;line-height:11px}
.coupon__code{position:absolute;left:64px;top:47px;width:80px;text-align:center;font-size:7px;line-height:9px;color:var(--ink)}
.coupon__code em{font-style:normal;color:var(--green);font-size:8.5px}
.cut-line{position:absolute;left:0;width:345px;border-top:1.2px dashed #9aa4a8}
</style>
</head>
<body>

<section class="flyer flyer--front" aria-label="Flyer Vorderseite">
  <div class="band-top"></div>
  <div class="hero-photo" role="img" aria-label="Foto eines zersplitterten Smartphone-Displays auf nassem Untergrund"></div>
  <div class="side-bar"></div>
  <div class="brand"><span class="brand__dot"></span>flickwerkstube</div>
  <div class="claim">PROFI REPARATUREN<span>IN IHRER NÄHE!</span></div>
  <div class="section-label">VORTEILE:</div>
  <div class="stoerer"><b>%</b>Gutscheine<br>nutzen und<br>sparen!</div>

  <ul class="benefits">
    <li class="benefit">
      <div class="benefit__icon"><svg width="22" height="22" viewBox="0 0 24 24" fill="none" stroke="#7dbb3a" stroke-width="1.6"><path d="M12 21s-6-6.2-6-11a6 6 0 0 1 12 0c0 4.8-6 11-6 11z"/><circle cx="12" cy="10" r="2.3"/></svg></div>
      <div class="benefit__title">KUNDENNÄHE</div>
      <div class="benefit__text">Finde eine Werkstatt in deiner Nähe</div>
      <div class="benefit__rule"></div>
    </li>
    <li class="benefit">
      <div class="benefit__icon"><svg width="22" height="22" viewBox="0 0 24 24" fill="none" stroke="#7dbb3a" stroke-width="1.6"><rect x="5" y="3" width="12" height="16" rx="1"/><path d="M8 8h6M8 11h6M8 14h4"/><path d="M17 7h2v14H8v-2"/></svg></div>
      <div class="benefit__title">VERGLEICH</div>
      <div class="benefit__text">Vergleiche Qualität und Preise der Werkstätten</div>
      <div class="benefit__rule"></div>
    </li>
    <li class="benefit">
      <div class="benefit__icon"><svg width="22" height="22" viewBox="0 0 24 24" fill="none" stroke="#7dbb3a" stroke-width="1.6"><ellipse cx="12" cy="13" rx="7" ry="5.5"/><path d="M8 18v2M16 18v2M19 12h2"/><circle cx="9.5" cy="7" r="2.2"/></svg></div>
      <div class="benefit__title">BEST PRICE</div>
      <div class="benefit__text">Online Best Price sichern &amp; lokal reparieren lassen</div>
      <div class="benefit__rule"></div>
    </li>
    <li class="benefit">
      <div class="benefit__icon"><svg width="22" height="22" viewBox="0 0 24 24" fill="none" stroke="#7dbb3a" stroke-width="1.6"><path d="M12 3l7 3v6c0 4.5-3 7.5-7 9-4-1.5-7-4.5-7-9V6z"/></svg></div>
      <div class="benefit__title">SICHERE ABWICKLUNG</div>
      <div class="benefit__text">Abgesichert durch den Kaufhort Siegel Käuferschutz</div>
      <div class="benefit__rule"></div>
    </li>
    <li class="benefit">
      <div class="benefit__icon"><svg width="22" height="22" viewBox="0 0 24 24" fill="none" stroke="#7dbb3a" stroke-width="1.6"><path d="M12 3l7 3v6c0 4.5-3 7.5-7 9-4-1.5-7-4.5-7-9V6z"/><circle cx="12" cy="12" r="3.5"/></svg></div>
      <div class="benefit__title">SICHERE ZAHLUNG</div>
      <div class="benefit__text">Sichere Bezahlung über MUNDOR Treuhandschutz</div>
    </li>
  </ul>

  <div class="seal-band"></div>
  <div class="seal seal--kaufhort" role="img" aria-label="Kaufhort Siegel Käuferschutz"></div>
  <div class="seal seal--mundor" role="img" aria-label="MUNDOR Treuhandschutz"></div>
  <div class="url-box">WWW.FLICKWERKSTUBE.DE</div>
  <div class="contacts">
    <div class="contact"><span class="contact__icon"><svg width="9" height="9" viewBox="0 0 24 24" fill="none" stroke="#7dbb3a" stroke-width="2.4"><path d="M12 21s-6-6.2-6-11a6 6 0 0 1 12 0c0 4.8-6 11-6 11z"/></svg></span><span>Lindenweg 12<br>80331 Musterstadt</span></div>
    <div class="contact"><span class="contact__icon"><svg width="9" height="9" viewBox="0 0 24 24" fill="none" stroke="#7dbb3a" stroke-width="2.4"><path d="M5 3h4l2 5-3 2a11 11 0 0 0 6 6l2-3 5 2v4a2 2 0 0 1-2 2A17 17 0 0 1 3 5a2 2 0 0 1 2-2z"/></svg></span><span>Telefon:<br>089 555017200</span></div>
    <div class="contact"><span class="contact__icon"><svg width="9" height="9" viewBox="0 0 24 24" fill="none" stroke="#7dbb3a" stroke-width="2.4"><rect x="3" y="5" width="18" height="14" rx="1"/><path d="M3 6l9 7 9-7"/></svg></span><span>E-Mail:<br>hallo@flickwerk.de</span></div>
  </div>
  <div class="band-bottom"></div>
</section>

<section class="flyer flyer--back" aria-label="Flyer Rückseite">
  <div class="cracks" role="img" aria-label="Feine Linien eines gesprungenen Displays als Hintergrund"></div>
  <div class="band-top"></div>
  <div class="brand"><span class="brand__dot"></span>flickwerkstube</div>
  <div class="section-label">GUTSCHEINE:</div>
  <p class="intro">Lorem ipsum dolor sit amet, consetetur sadipscing elitr, sed diam nonumy eirmod tempor invidunt ut labore et dolore magna aliquyam erat, sed diam voluptua.</p>

  <div class="coupon" style="left:19px;top:218px"><div class="coupon__box"></div><div class="coupon__value"><b>10€</b><span>RABATT</span></div><div class="coupon__offer">AUF DISPLAY REPARATUREN</div><div class="coupon__code">Gutscheincode:<br><em>10XMaiX2019</em></div></div>
  <div class="coupon" style="left:187px;top:218px"><div class="coupon__box"></div><div class="coupon__value"><b>10%</b><span>RABATT</span></div><div class="coupon__offer">AUF DISPLAY REPARATUREN</div><div class="coupon__code">Gutscheincode:<br><em>10XMaiX2019</em></div></div>

  <div class="cut-line" style="top:318px"></div>

  <div class="coupon" style="left:19px;top:347px"><div class="coupon__box"></div><div class="coupon__value"><b>10%</b><span>RABATT</span></div><div class="coupon__offer">AUF VELKOR MODELLE</div><div class="coupon__code">Gutscheincode:<br><em>10XMaiX2019</em></div></div>
  <div class="coupon" style="left:187px;top:347px"><div class="coupon__box"></div><div class="coupon__value"><b>10€</b><span>RABATT</span></div><div class="coupon__offer">AUF DISPLAY REPARATUREN</div><div class="coupon__code">Gutscheincode:<br><em>10XMaiX2019</em></div></div>

  <div class="cut-line" style="top:450px"></div>

  <div class="coupon" style="left:19px;top:482px"><div class="coupon__box"></div><div class="coupon__value"><b>10€</b><span>RABATT</span></div><div class="coupon__offer">AUF DISPLAY REPARATUREN</div><div class="coupon__code">Gutscheincode:<br><em>10XMaiX2019</em></div></div>
  <div class="coupon" style="left:187px;top:482px"><div class="coupon__box"></div><div class="coupon__value"><b>10%</b><span>RABATT</span></div><div class="coupon__offer">AUF DISPLAY REPARATUREN</div><div class="coupon__code">Gutscheincode:<br><em>10XMaiX2019</em></div></div>

  <div class="seal-band"></div>
  <div class="seal seal--kaufhort" role="img" aria-label="Kaufhort Siegel Käuferschutz"></div>
  <div class="seal seal--mundor" role="img" aria-label="MUNDOR Treuhandschutz"></div>
  <div class="url-box">WWW.FLICKWERKSTUBE.DE</div>
  <div class="contacts">
    <div class="contact"><span class="contact__icon"><svg width="9" height="9" viewBox="0 0 24 24" fill="none" stroke="#7dbb3a" stroke-width="2.4"><path d="M12 21s-6-6.2-6-11a6 6 0 0 1 12 0c0 4.8-6 11-6 11z"/></svg></span><span>Lindenweg 12<br>80331 Musterstadt</span></div>
    <div class="contact"><span class="contact__icon"><svg width="9" height="9" viewBox="0 0 24 24" fill="none" stroke="#7dbb3a" stroke-width="2.4"><path d="M5 3h4l2 5-3 2a11 11 0 0 0 6 6l2-3 5 2v4a2 2 0 0 1-2 2A17 17 0 0 1 3 5a2 2 0 0 1 2-2z"/></svg></span><span>Telefon:<br>089 555017200</span></div>
    <div class="contact"><span class="contact__icon"><svg width="9" height="9" viewBox="0 0 24 24" fill="none" stroke="#7dbb3a" stroke-width="2.4"><rect x="3" y="5" width="18" height="14" rx="1"/><path d="M3 6l9 7 9-7"/></svg></span><span>E-Mail:<br>hallo@flickwerk.de</span></div>
  </div>
  <div class="band-bottom"></div>
</section>

</body>
</html>
```